Web design - holistic filmmaker

I need a design for my new website.

I am a holistic filmmaker, ie I make films for healers, alternative practitioners, spiritual people and institutions that offer training in this field.

The design should be noble, bright, convey the feeling of space and expanse and have some particularly beautiful color accents.

The structure is: start page, offer, references, about me, imprint.

As an idea for the start page, I thought that either I could introduce myself as a filmmaker and my offer, or we could start right on the start page with the references, ie photos and links to already realized projects.

If you want more information or an exchange, I'd love to hear from you. At the moment I just don't know how to describe it better.

The winner will then be asked to design a logo.

Target Market(s)

healers, alternative practitioners, spiritual people and institutions that offer training in this field

Industry/Entity Type

Film production

Number of Pages Required

3 page

```html
<!DOCTYPE html>
<html lang="en">
<head>
<meta charset="utf-8">
<title>Marek – Holistic Filmmaker</title>
<link rel="stylesheet" href="https://fonts.googleapis.com/css2?family=Outfit:wght@400;500;600;700&display=swap">
<style>
  :root {
    --ink: #111111;
    --white: #ffffff;
    --hero-bg: #d3cdc8;
    --photo-dark: #3a3634;
    --photo-mid: #8d8883;
    --teal: #7cc6c8;
    --teal-soft: #d8eff0;
    --grey-soft: #e4e4e4;
    --cream: #faf0e1;
    --footer: #000000;
    --play: rgba(20,20,20,0.55);
  }
  * { margin: 0; padding: 0; box-sizing: border-box; }
  html, body { width: 1200px; height: 2282px; overflow: hidden; }
  body { position: relative; background: var(--white); color: var(--ink); font-family: "Outfit", sans-serif; }

  /* header */
  .site-header { position: absolute; left: 0; top: 0; width: 1200px; height: 97px; background: var(--white); }
  .brand { position: absolute; left: 161px; top: 18px; }
  .brand-name { font-size: 40px; font-weight: 700; letter-spacing: 14px; line-height: 40px; }
  .brand-tag { font-size: 14px; font-weight: 500; line-height: 16px; margin-top: 3px; letter-spacing: 0.2px; }
  .nav { position: absolute; top: 40px; left: 0; width: 1200px; height: 20px; }
  .nav a { position: absolute; font-size: 13px; font-weight: 500; color: inherit; text-decoration: none; line-height: 16px; }

  /* hero */
  .hero { position: absolute; left: 0; top: 97px; width: 1200px; height: 560px; background: var(--hero-bg); overflow: hidden; }
  .hero-photo { position: absolute; left: 470px; top: 0; width: 730px; height: 560px;
    background: radial-gradient(ellipse 60% 70% at 62% 40%, #bdb6b0 0%, #8d8883 40%, #3a3634 80%);
    -webkit-mask-image: linear-gradient(90deg, transparent 0%, #000 30%);
    mask-image: linear-gradient(90deg, transparent 0%, #000 30%); }
  .hero-wave { position: absolute; left: 0; top: 0; }
  .hero-title { position: absolute; left: 162px; top: 113px; font-size: 56px; font-weight: 700; line-height: 68px; letter-spacing: -0.5px; }
  .hero-lead { position: absolute; left: 163px; top: 251px; font-size: 21px; font-weight: 400; line-height: 28px; }
  .btn-outline { position: absolute; display: flex; align-items: center; justify-content: center; border: 2px solid var(--ink); background: transparent; font-size: 13px; font-weight: 500; color: var(--ink); }

  /* references */
  .deco-ring { position: absolute; left: 86px; top: 686px; width: 156px; height: 156px; border-radius: 50%;
    background: radial-gradient(circle, transparent 38%, #e9e9e9 40%, #f3f3f3 70%, transparent 71%); }
  .arrow { position: absolute; top: 825px; width: 36px; height: 36px; border-radius: 50%; }
  .arrow-prev { left: 78px; background: var(--grey-soft); }
  .arrow-next { left: 1076px; background: var(--teal-soft); }
  .arrow svg { position: absolute; }
  .ref-card { position: absolute; top: 750px; width: 279px; }
  .ref-media { position: relative; width: 279px; height: 186px; border-radius: 8px; overflow: hidden; }
  .ref-play { position: absolute; left: 50%; top: 50%; width: 46px; height: 46px; margin: -23px 0 0 -23px; border-radius: 50%; background: var(--play); }
  .ref-play::after { content: ""; position: absolute; left: 18px; top: 14px; border-left: 15px solid var(--white); border-top: 9px solid transparent; border-bottom: 9px solid transparent; }
  .ref-badge { position: absolute; top: 10px; right: -10px; width: 56px; height: 56px; border-radius: 50%; background: var(--white); }
  .ref-text { padding: 18px 18px 0; font-size: 14.5px; line-height: 22.5px; height: 102px; }
  .ref-rule { height: 2px; background: var(--teal); }
  .btn-dark { position: absolute; left: 536px; top: 1080px; width: 128px; height: 45px; background: var(--ink); color: var(--white); display: flex; align-items: center; justify-content: center; gap: 8px; font-size: 13px; font-weight: 500; }

  /* journey */
  .journey { position: absolute; left: 0; top: 1216px; width: 1200px; height: 476px; background: var(--cream); overflow: hidden; }
  .journey-title { position: absolute; left: 0; top: 82px; width: 1200px; text-align: center; font-size: 32px; font-weight: 700; line-height: 40px; }
  .journey-copy { position: absolute; left: 222px; top: 130px; width: 756px; text-align: center; font-size: 18px; line-height: 27px; }
  .journey-copy p + p { margin-top: 10px; }
  .color-band { position: absolute; left: 133px; top: 330px; width: 945px; height: 146px;
    background: linear-gradient(90deg, #e46a72 0%, #e0472f 20%, #f1b52a 38%, #3fae4a 52%, #2f86dc 68%, #7a3cc4 84%, #c57ab8 100%); }

  /* customers */
  .customers-title { position: absolute; left: 0; top: 1774px; width: 1200px; text-align: center; font-size: 33px; font-weight: 700; line-height: 40px; }
  .client { position: absolute; top: 1873px; width: 220px; height: 80px; display: flex; align-items: center; justify-content: center; gap: 10px; font-size: 21px; font-weight: 500; color: #6b2a2e; white-space: nowrap; }
  .client-dot { flex: none; width: 22px; height: 22px; border-radius: 50%; background: #c2353b; }

  /* footer */
  .site-footer { position: absolute; left: 0; top: 2063px; width: 1200px; height: 219px; background: var(--footer); color: var(--white); }
  .site-footer .brand { left: 163px; top: 50px; }
  .site-footer .nav { top: 69px; }
  .copyright { position: absolute; left: 163px; top: 137px; font-size: 11.5px; line-height: 14px; }
  .social { position: absolute; top: 131px; width: 26px; height: 26px; border-radius: 50%; border: 1.5px solid var(--white); }
  .social.filled { background: var(--white); }
</style>
</head>
<body>

<header class="site-header">
  <div class="brand">
    <div class="brand-name">MAREK</div>
    <div class="brand-tag">HOLISTIC FILMMAKER</div>
  </div>
  <nav class="nav">
    <a style="left:541px">START PAGE</a>
    <a style="left:665px">OFFER</a>
    <a style="left:747px">REFERENCES</a>
    <a style="left:876px">ABOUT ME</a>
    <a style="left:986px">IMPRINT</a>
  </nav>
</header>

<section class="hero">
  <div class="hero-photo" role="img" aria-label="Black and white portrait of the filmmaker"></div>
  <svg class="hero-wave" width="1200" height="560" viewBox="0 0 1200 560" aria-hidden="true">
    <path d="M0 537 C120 480 240 465 340 470 C520 478 700 555 880 550 C1000 546 1120 520 1200 488 L1200 560 L0 560 Z" fill="#ffffff"/>
  </svg>
  <h1 class="hero-title">My Name Is Marek<br>And I Do Movies.</h1>
  <p class="hero-lead">With enthusiasm and wholeheartedly.<br>I am a holistic filmmaker.</p>
  <div class="btn-outline" style="left:160px; top:326px; width:129px; height:46px;">READ MORE</div>
</section>

<div class="deco-ring" aria-hidden="true"></div>

<div class="arrow arrow-prev">
  <svg width="36" height="36" viewBox="0 0 36 36"><path d="M30 19 H9 M17 10 L8 19 L17 28" fill="none" stroke="#333" stroke-width="2.4"/></svg>
</div>
<div class="arrow arrow-next">
  <svg width="36" height="36" viewBox="0 0 36 36"><path d="M0 18 H27 M19 9 L28 18 L19 27" fill="none" stroke="#5cb8bb" stroke-width="2.4"/></svg>
</div>

<article class="ref-card" style="left:161px">
  <div class="ref-media" role="img" aria-label="Video still of a woman presenting at a flip chart" style="background:linear-gradient(120deg,#8a5a55 0%,#c14f86 45%,#d9d2c6 100%)">
    <span class="ref-play"></span>
  </div>
  <p class="ref-text">Ut wisi enim ad minim vam nostrud exerci tation ullamcorper suscipi lobortis nisl ut aliquip.</p>
  <div class="ref-rule"></div>
</article>

<article class="ref-card" style="left:460px">
  <div class="ref-media" role="img" aria-label="Video still of a healing session in a bright room" style="background:linear-gradient(120deg,#5a4f4a 0%,#a58f86 45%,#c9394a 80%,#c7b9a8 100%)">
    <span class="ref-play"></span>
    <span class="ref-badge" style="background:#f2e4e0"></span>
  </div>
  <p class="ref-text">Ut wisi enim ad minim vam nostrud exerci tation ullamcorper suscipi lobortis nisl ut aliquip.</p>
  <div class="ref-rule"></div>
</article>

<article class="ref-card" style="left:760px">
  <div class="ref-media" role="img" aria-label="Video still of a singer performing outdoors" style="background:linear-gradient(120deg,#6c7a4c 0%,#4d4a3c 40%,#8a8774 75%,#5b6a43 100%)">
    <span class="ref-play"></span>
    <span class="ref-badge"></span>
  </div>
  <p class="ref-text">Ut wisi enim ad minim vam nostrud exerci tation ullamcorper suscipi lobortis nisl ut aliquip.</p>
  <div class="ref-rule"></div>
</article>

<div class="btn-dark">SEE ALL
  <svg width="12" height="8" viewBox="0 0 12 8"><path d="M1 1 L6 6 L11 1" fill="none" stroke="#fff" stroke-width="1.5"/></svg>
</div>

<section class="journey">
  <h2 class="journey-title">Making A Movie Is Always A Journey To Yourself.</h2>
  <div class="journey-copy">
    <p>Lightpath Films is aimed at all people and institutions whose striving for truthfulness is the driving force behind their actions.</p>
    <p>I accompany you on the way to portraying your essence, with simple means and without special effects.</p>
  </div>
  <div class="color-band" role="img" aria-label="Colourful powder splash illustration"></div>
  <div class="btn-outline" style="left:536px; top:273px; width:129px; height:46px;">READ MORE</div>
</section>

<h2 class="customers-title">CUSTOMERS</h2>
<div class="client" style="left:169px; color:#222;">Lumen Sol</div>
<div class="client" style="left:393px;"><span class="client-dot"></span>innerweg.de</div>
<div class="client" style="left:604px; color:#c2353b;"><span class="client-dot" style="background:#e04a2a"></span>Kalon Vital</div>
<div class="client" style="left:804px; color:#4a3a8c;"><span class="client-dot" style="background:#6b3fa0"></span>Aurora Festspiele</div>

<footer class="site-footer">
  <div class="brand">
    <div class="brand-name">MAREK</div>
    <div class="brand-tag">HOLISTIC FILMMAKER</div>
  </div>
  <nav class="nav">
    <a style="left:542px">START PAGE</a>
    <a style="left:666px">OFFER</a>
    <a style="left:748px">REFERENCES</a>
    <a style="left:877px">ABOUT ME</a>
    <a style="left:987px">IMPRINT</a>
  </nav>
  <p class="copyright">© 2023 Marek Holistic Filmmaker. All Rights Reserved.</p>
  <span class="social" style="left:915px" aria-label="Social link"></span>
  <span class="social filled" style="left:947px" aria-label="Social link"></span>
  <span class="social" style="left:980px" aria-label="Social link"></span>
  <span class="social" style="left:1013px" aria-label="Social link"></span>
</footer>

</body>
</html>
```